Inspiration Poster

Inspirational Poster that has a Dorin Velk like abstract look (http://www.quorvix.com/images/search?q=dorin+velk&FORM=HDRSC2) with the text:

"we walk not in order to arrive at the promise land but because walking itself is a revolution"
-Mark Fennimore

```html
<!DOCTYPE html>
<html lang="en">
<head>
<meta charset="utf-8">
<title>Inspiration Poster – Walking Is a Revolution</title>
<link href="https://fonts.googleapis.com/css2?family=Arimo:wght@400;700&family=Josefin+Sans:wght@600&display=swap" rel="stylesheet">
<style>
  :root {
    --ink-white: #ffffff;
    --panel: rgba(38, 38, 40, 0.84);
    --deep-plum: #2a0f24;
    --ember: #b5471a;
    --rust: #6b2a12;
    --teal: #3fa6c4;
    --ice: #cfe6ee;
    --night: #0f1a2a;
  }
  html, body {
    margin: 0;
    padding: 0;
    width: 849px;
    height: 1200px;
    overflow: hidden;
    background: var(--night);
  }
  .poster {
    position: relative;
    width: 849px;
    height: 1200px;
    overflow: hidden;
  }
  .poster__backdrop {
    position: absolute;
    inset: 0;
    background:
      radial-gradient(ellipse 420px 90px at 560px 830px, rgba(235,240,240,0.55), transparent 70%),
      radial-gradient(ellipse 300px 80px at 180px 800px, rgba(240,210,170,0.45), transparent 70%),
      radial-gradient(ellipse 360px 200px at 640px 220px, rgba(95,190,215,0.85), transparent 70%),
      radial-gradient(ellipse 300px 160px at 760px 560px, var(--ice), transparent 70%),
      radial-gradient(ellipse 380px 220px at 120px 120px, rgba(160,60,40,0.75), transparent 70%),
      radial-gradient(ellipse 300px 300px at 60px 440px, rgba(70,20,80,0.8), transparent 70%),
      radial-gradient(ellipse 500px 200px at 300px 1120px, rgba(190,80,25,0.9), transparent 70%),
      radial-gradient(ellipse 400px 220px at 720px 1080px, rgba(120,70,40,0.85), transparent 70%),
      linear-gradient(180deg, var(--deep-plum) 0%, #1d2a3a 40%, var(--teal) 60%, var(--rust) 85%, #3a1a0c 100%);
  }
  .quote-panel {
    position: absolute;
    left: 188px;
    top: 402px;
    width: 487px;
    height: 485px;
    background: var(--panel);
  }
  .quote {
    position: absolute;
    left: 0;
    right: 0;
    top: 108px;
    margin: 0;
    color: var(--ink-white);
    font-family: "Arimo", Arial, sans-serif;
    font-weight: 700;
    font-size: 44px;
    line-height: 48.5px;
    letter-spacing: -0.5px;
    text-align: center;
  }
  .quote__line { display: block; }
  .quote__accent {
    font-family: "Josefin Sans", sans-serif;
    font-weight: 600;
    font-size: 42px;
    letter-spacing: 4px;
    text-transform: uppercase;
    line-height: 58px;
  }
  .quote__close {
    font-family: "Arimo", Arial, sans-serif;
    font-weight: 700;
    letter-spacing: 0;
  }
  .attribution {
    position: absolute;
    right: 8px;
    bottom: 3px;
    margin: 0;
    color: var(--ink-white);
    font-family: "Arimo", Arial, sans-serif;
    font-weight: 400;
    font-size: 14px;
  }
</style>
</head>
<body>
  <main class="poster">
    <div class="poster__backdrop" role="img" aria-label="Abstract long-exposure photograph of blurred light streaks in teal, plum, orange and white"></div>
    <section class="quote-panel">
      <blockquote class="quote">
        <span class="quote__line">“we walk not in</span>
        <span class="quote__line">order to arrive at</span>
        <span class="quote__line">the promise land</span>
        <span class="quote__line">but because</span>
        <span class="quote__line">walking itself is a</span>
        <span class="quote__line quote__accent">revolution<span class="quote__close">”</span></span>
      </blockquote>
      <p class="attribution">Mark Fennimore</p>
    </section>
  </main>
</body>
</html>
```